Night Dresses business cards business requirers

We are a new company initiating Mexico operations. Our core business is Night woman dress (both formal and party dress) for rent. Gownvella is the name of the company. ITS Gownvella form by two word. The dress word and topia (Utopic) so the place Gownvella Means That You cant get the ideal, perfect and unique dress for your event. So we would like a modern, very creative, and attractive business card.

Industry/Entity Type

Womens Clothing

Contact Information for Business Card

Rounded Borders, two faces

Requirements
Must have
• Rounded borders, logo and slogan, modern, glam, attractive design
Should not have
• modern design classic or not

```html
<!DOCTYPE html>
<html lang="en">
<head>
<meta charset="UTF-8">
<title>Gownvella Business Card</title>
<link href="https://fonts.googleapis.com/css2?family=Montserrat:wght@400;500;600&family=Arimo:wght@400&display=swap" rel="stylesheet">
<style>
  :root {
    --bg: #e4e4e6;
    --orchid: #b35f9b;
    --arc-grey: #6f6f71;
    --paper: #ffffff;
    --charcoal: #424244;
    --ink: #5a5a5c;
    --ink-soft: #7a7a7c;
  }
  * { margin: 0; padding: 0; box-sizing: border-box; }
  html, body { width: 1200px; height: 950px; overflow: hidden; }
  body {
    background: var(--bg);
    display: flex;
    align-items: center;
    justify-content: center;
    gap: 80px;
    font-family: "Arimo", Arial, sans-serif;
  }
  .card {
    position: relative;
    width: 400px;
    height: 680px;
    border-radius: 20px;
    overflow: hidden;
    box-shadow: 0 10px 28px rgba(0,0,0,0.18);
  }
  .card-front { background: var(--paper); }
  .card-back { background: var(--charcoal); }

  .front-band { position: absolute; top: 0; left: 0; width: 400px; height: 300px; }
  .holder {
    position: absolute;
    top: 44px;
    right: 34px;
    color: #fff;
    font-family: "Montserrat", Arial, sans-serif;
    font-size: 17px;
    letter-spacing: 0.5px;
  }
  .holder .name { font-weight: 600; }
  .holder .role { font-weight: 400; }

  .brand {
    display: flex;
    align-items: center;
    gap: 16px;
  }
  .brand-circle {
    border-radius: 50%;
    border: 2px solid currentColor;
    flex: none;
  }
  .brand-name {
    font-family: "Montserrat", Arial, sans-serif;
    font-weight: 500;
    letter-spacing: 6px;
    text-transform: uppercase;
  }

  .front-brand {
    position: absolute;
    left: 38px;
    top: 340px;
    color: var(--orchid);
  }
  .front-brand .brand-circle { width: 58px; height: 58px; }
  .front-brand .brand-name { font-size: 24px; color: var(--ink); }

  .address {
    position: absolute;
    left: 38px;
    top: 440px;
    color: var(--ink-soft);
    font-size: 14px;
    line-height: 21px;
  }
  .contacts {
    position: absolute;
    left: 38px;
    top: 500px;
    list-style: none;
    color: var(--ink);
    font-size: 14px;
  }
  .contacts li {
    display: flex;
    align-items: center;
    gap: 12px;
    height: 26px;
  }
  .contacts svg { width: 14px; height: 14px; fill: var(--orchid); flex: none; }

  .back-brand {
    position: absolute;
    inset: 0;
    justify-content: center;
    flex-direction: column;
    color: #fff;
  }
  .back-brand .brand-circle { width: 96px; height: 96px; }
  .back-brand .brand-name { font-size: 30px; margin-top: 26px; }
</style>
</head>
<body>
  <section class="card card-front">
    <svg class="front-band" viewBox="0 0 400 300" aria-hidden="true">
      <path d="M0 0 H400 V70 C280 80 120 150 0 290 V0 Z" fill="var(--orchid)"/>
      <path d="M400 70 C280 80 120 150 0 290 V300 C120 165 280 92 400 84 Z" fill="var(--arc-grey)"/>
    </svg>
    <p class="holder"><span class="name">MARA LENK</span> <span class="role">- PRESIDENT</span></p>

    <div class="brand front-brand">
      <span class="brand-circle"></span>
      <p class="brand-name">Gownvella</p>
    </div>

    <p class="address">4120 Larkspur Avenue<br>Cedar Glen, NY 11409</p>

    <ul class="contacts">
      <li><svg viewBox="0 0 16 16"><path d="M3 1h3l1 4-2 1c1 2 3 4 5 5l1-2 4 1v3c0 1-1 2-2 2C7 15 1 9 1 3c0-1 1-2 2-2z"/></svg>555 0142 7781</li>
      <li><svg viewBox="0 0 16 16"><path d="M4 0h8a1 1 0 0 1 1 1v14a1 1 0 0 1-1 1H4a1 1 0 0 1-1-1V1a1 1 0 0 1 1-1zm1 2v10h6V2z"/></svg>555 0178 6024</li>
      <li><svg viewBox="0 0 16 16"><path d="M4 0h7v4H4zM1 5h14v8h-3v3H4v-3H1zm4 6v3h6v-3z"/></svg>555 0196 4417</li>
      <li><svg viewBox="0 0 16 16"><path d="M1 3h14v10H1zm1 1v1l6 4 6-4V4z"/></svg>mara@example.com</li>
      <li><svg viewBox="0 0 16 16"><circle cx="8" cy="8" r="7"/></svg>www.example.com</li>
    </ul>
  </section>

  <section class="card card-back">
    <div class="brand back-brand">
      <span class="brand-circle"></span>
      <p class="brand-name">Gownvella</p>
    </div>
  </section>
</body>
</html>
```